Office Wall Poster plus other Wall Decal quotes in office

We have redesigned our office & require parts of our Culture statement to be displayed in our office. Our company is VOLO Estate Agents Group and our brand is all about being VOLO .. integrity, honesty, authenticity etc.
We have two areas we wish to decorate.
1. Reception
2. Meeting Room

RECEPTION
We want our leading culture statement to be displayed as large A0 size in a framed POSTER PRINT in our reception. The frame will be black.
WORDING: 'There's a reason we're called VOLO. VOLO is the essence of who we are'
Our brand colors are red, white, black. Our Red is CMYK 12,99, 92,02
When we type our name VOLO, we always use Venera font (always in caps). I have attached a file I personally created with 3 different ideas (I am not a designer) but we are not happy with any of them but it will give you an idea of what we are looking for. We want a simple statement so it stands out and not too busy.

MEETING ROOM
We have one black feature wall in this room and wish to dress this with a collection of quotes from our main Culture statement. We will have these printed as 'stick on wall decals' We have provided a collection of 8 quotes for you to design. Wording is to be in white colour with the key words to be METALLIC SILVER & in caps. We were planning to arrange them ad-hoc on the wall singularly, but if you have any creative ideas on how to display these, we are open to suggestions. Please provide your ideas on how best to arrange these on the black wall. Maybe even in a circle to represent our logo? But we truly do not have a clue - we are only real estate agents, not designers. That is why we would love suggetions on how best to make our Culture Statements work best.
Best of luck and we are excited to see your ideas!

Our clients need to get a great feel for what we are all about when they visit our office. Our culture needs to be seen and felt.

Real Estate

• We use Venera font when we type our name VOLO

EB3D1F
EC4F4E
F09395
F8D3D4
FCEDEE

• Not too busy, simple statements, easy to read

```html
<!DOCTYPE html>
<html lang="en">
<head>
<meta charset="utf-8">
<title>VOLO Culture Statement Poster</title>
<link rel="stylesheet" href="https://fonts.googleapis.com/css2?family=Michroma&family=Jura:wght@600&family=Playfair+Display:wght@900&display=swap">
<style>
  :root {
    --brand-red: #C8202F;
    --statement-grey: #8E8E8E;
    --fabric-light: #F4F1EE;
    --fabric-mid: #E6E1DB;
    --fabric-warm: #EFE2CC;
  }
  html, body {
    margin: 0;
    padding: 0;
    overflow: hidden;
  }
  .poster {
    position: relative;
    width: 1200px;
    height: 1000px;
    overflow: hidden;
    background: var(--fabric-light);
  }
  .fabric-backdrop {
    position: absolute;
    inset: 0;
    background:
      radial-gradient(ellipse 420px 520px at 30% 35%, var(--fabric-warm) 0%, rgba(239,226,204,0) 70%),
      linear-gradient(135deg, var(--fabric-mid) 0%, var(--fabric-light) 45%, var(--fabric-mid) 100%);
  }
  .quote-mark {
    position: absolute;
    font-family: 'Playfair Display', serif;
    font-weight: 900;
    color: var(--brand-red);
    line-height: 1;
  }
  .quote-mark--open {
    left: 120px;
    top: 250px;
    font-size: 300px;
  }
  .quote-mark--close {
    left: 965px;
    top: 640px;
    font-size: 300px;
  }
  .statement {
    position: absolute;
    left: 230px;
    top: 360px;
    width: 740px;
  }
  .statement__lead,
  .statement__bridge {
    font-family: 'Jura', sans-serif;
    font-weight: 600;
    color: var(--statement-grey);
    margin: 0;
    white-space: nowrap;
  }
  .statement__lead {
    font-size: 38px;
    letter-spacing: 1px;
    padding-left: 30px;
  }
  .statement__name {
    font-family: 'Michroma', sans-serif;
    color: var(--brand-red);
    font-size: 168px;
    line-height: 1;
    margin: 4px 0 0;
    letter-spacing: 4px;
  }
  .statement__bridge {
    font-size: 58px;
    line-height: 1.1;
    margin-top: 10px;
    letter-spacing: 1px;
  }
  .statement__close {
    font-family: 'Michroma', sans-serif;
    color: var(--brand-red);
    font-size: 62px;
    line-height: 1;
    margin: 2px 0 0;
    white-space: nowrap;
  }
</style>
</head>
<body>
  <main class="poster">
    <div class="fabric-backdrop" role="img" aria-label="Close-up photograph of soft folded cream fabric"></div>
    <span class="quote-mark quote-mark--open" aria-hidden="true">&ldquo;</span>
    <section class="statement">
      <p class="statement__lead">There's a reason we're called</p>
      <h1 class="statement__name">VOLO</h1>
      <p class="statement__bridge">VOLO is the essence of</p>
      <p class="statement__close">WHO WE ARE</p>
    </section>
    <span class="quote-mark quote-mark--close" aria-hidden="true">&rdquo;</span>
  </main>
</body>
</html>
```